Verpackungsdesign für Kaffeerösterei
Zielgruppe
wir Rösten Kaffee. Wir haben uns darauf Spezialisiert Hochwertigen Premium Caffe Crema herzustellen und bieten auch nur diesen in Unserem Shop www.brunor7-kaffee.de an. wir bieten 250gr. 500gr. Kaffee an. .
Es kann gerne verrückt oder anders sein, dennoch aber sehr edel.
die Zielgruppe ist weitgestreut, aber laut unserern Daten ist die Ideale Zielgruppe der 52 Jährige Mann, der Wert auf Hochwertige Genussmittel legt und auch bereit ist mehr Geld dafür zu bezahlen.
ich habe bereits ein beispiel design und die Druckvorlage bereitgestellt.
Aufgabenstellung
das Konzept unserer Internetseite sollte berücksichtigt werden, ansonsten ist dem Kreativen kopf keine Grenzen gesetzt.

```html
<!DOCTYPE html>
<html lang="de">
<head>
<meta charset="utf-8">
<title>Brunor 7 – Cafe Crema 500g</title>
<link rel="stylesheet" href="https://fonts.googleapis.com/css2?family=Anton&family=Oswald:wght@400;700&display=swap">
<style>
  :root {
    --backdrop: #d9d9d9;
    --bag-black: #050505;
    --label-orange: #ee8300;
    --bean-stripe: #b0561e;
    --ink-dark: #231815;
    --text-grey: #a6a6a6;
    --smoke-blue: #6fa9bd;
    --smoke-night: #0d1a22;
    --seal-brown: #3a2614;
  }
  * { margin: 0; padding: 0; box-sizing: border-box; }
  html, body { width: 840px; height: 1200px; overflow: hidden; background: var(--backdrop); }
  .canvas { position: relative; width: 840px; height: 1200px; }
  .bag-front {
    position: absolute; left: 97px; top: 0; width: 646px; height: 1200px;
    background: var(--bag-black);
  }
  .bag-art { position: absolute; inset: 0; }
  .brand {
    position: absolute; left: 0; width: 646px; top: 370px;
    text-align: center; font-family: "Oswald", sans-serif; font-weight: 700;
    font-size: 54px; letter-spacing: 2px; color: var(--ink-dark); line-height: 1;
  }
  .product-name {
    position: absolute; left: 141px; top: 512px; width: 370px;
    font-family: "Anton", sans-serif; font-size: 78px; line-height: 1;
    color: var(--ink-dark); letter-spacing: -1px; text-align: center;
  }
  .tasting-notes {
    position: absolute; right: 278px; top: 592px; text-align: right;
    font-family: "Oswald", sans-serif; font-weight: 400; font-size: 21px;
    line-height: 31px; color: var(--ink-dark);
  }
  .profile {
    position: absolute; left: 224px; top: 950px;
    font-family: "Oswald", sans-serif; font-size: 24px; line-height: 35px;
    color: var(--text-grey); border-collapse: collapse;
  }
  .profile td { padding: 0 14px 0 0; }
  .profile .stars { letter-spacing: 2px; font-size: 22px; }
  .net-weight {
    position: absolute; left: 0; width: 646px; top: 1104px; text-align: center;
    font-family: "Oswald", sans-serif; font-weight: 700; font-size: 44px;
    color: var(--text-grey); line-height: 1;
  }
</style>
</head>
<body>
<div class="canvas">
  <div class="bag-front">
    <svg class="bag-art" width="646" height="1200" viewBox="0 0 646 1200">
      <defs>
        <linearGradient id="smoke-tone" x1="0" y1="0" x2="1" y2="1">
          <stop offset="0" stop-color="var(--smoke-night)"/>
          <stop offset="0.5" stop-color="var(--smoke-blue)" stop-opacity="0.55"/>
          <stop offset="1" stop-color="var(--smoke-night)"/>
        </linearGradient>
        <clipPath id="label-clip"><circle cx="321" cy="531" r="287"/></clipPath>
      </defs>
      <rect class="steam-photo" x="90" y="0" width="355" height="298" fill="url(#smoke-tone)"
            role="img" aria-label="Foto: bläulicher Kaffeedampf vor dunklem Hintergrund"/>
      <g class="speech-label">
        <circle cx="321" cy="531" r="287" fill="var(--label-orange)"/>
        <path d="M358 810 L344 880 C 390 875, 420 840, 448 794 Z" fill="var(--label-orange)"/>
      </g>
      <path class="bean-stripe" clip-path="url(#label-clip)" fill="var(--bean-stripe)"
            d="M283 250 C 340 330, 360 420, 320 520 C 280 620, 250 700, 262 815 L 300 815 C 285 700, 310 620, 345 520 C 385 420, 365 320, 310 250 Z"/>
      <circle class="seal" cx="422" cy="627" r="48" fill="var(--seal-brown)" stroke="#c9a24a" stroke-width="4"/>
    </svg>
    <div class="brand">BRUNOR 7</div>
    <div class="product-name">CAFE CREMA</div>
    <div class="tasting-notes">Geschmacksnote:<br>Dunkle Schokolade,<br>karamell</div>
    <table class="profile">
      <tr><td>Säure</td><td class="stars">✶✶</td></tr>
      <tr><td>Körper</td><td class="stars">✶✶✶</td></tr>
      <tr><td>Stärke</td><td class="stars">✶✶✶✶✶</td></tr>
    </table>
    <div class="net-weight">Net wt. 500g</div>
  </div>
</div>
</body>
</html>
```